Cover for nonfiction/memoir book "The Hidden Weather Within"

Revisions only please.

We're looking for a *nonfiction* *memoir* look that is consistent with other covers in that genre.

MUST HAVE:
- It must include the BACK COVER as it will be for print as well as an ebook.
- Title: The Hidden Weather Within
- TITLE MUST BE EASILY READ AT BRINDLECART THUMBNAIL SIZE
- Author name: Dorothea Quill
- At least one of the attached photos of Dorothea
- In COLOR
- The synopsis below
- Space for an endorsement

From the author: "I am looking for a cover that is eye catching and interesting or artistic, rather than just glamorous or pretty. If you like to edit the photos please do not completely remove the wrinkle between my eyebrows as I mention this in the book. It is okay if i look non conventional and my inner Aspie shows a little. The book is a little bit girly, and it would be good for the cover to reflect that, but mildly. No bright pink and purple designs. Please feel free to zoom in or crop the photos as you think works best"

SYNOPSIS (needs to go on the back cover)

The Hidden Weather Within is an acutely honest and often highly entertaining memoir by Dorothea Quill about life with Asperger's Syndrome. The book follows Dorothea in exploring her past and takes the reader with her on her journey to receiving and accepting her diagnosis. Instead of rehashing widely available Asperger's information, Dorothea focuses on discussing the thoughts, feelings and ideas that go along with being an Aspie, giving us a rare peek into what it really feels like to be a person on the spectrum. A must read for all those who enjoy deep personal stories or have a loved one on the spectrum that they wish to understand better.

The book dimensions will be 5x8 trade paperback and 6x9 hardcover (plus 0.25 bleed margin on all sizes - for both sizes).
Here is some more information from the publisher on cover requirements:

"I've attached a sample of both a paperback and hardcover size. Note that the spine width will be different depending on the final length of the book, so it won't be exact. That said, the front and back covers, and the flaps (for the hardcover) will always be the same as shown.
For deliverables, we need the following:

a Creative Suite 6 or earlier native .PSD (Photoshop), .ID (InDesign), or .AI (Illustrator) file. Creative Cloud files cannot be used and will not be accepted.
final file must include layered objects, and cannot be one 'background' image
Final files must be in CMYK color mode, 300dpi minimum
Total Ink saturation must be no more than 240% on any part of the cover. "True" black should use the following CMYK values: 60/40/40/100.
Fonts used in creation of the cover must be either A) embedded or B) sent with the final file
Vector art is preferred for scaling purposes"

Target Market(s)

Women of all ages. People who like psychology and personal stories.
Also parents and family members who may have a loved one on the Autism spectrum.

Requirements
Nice to have
• Bright green new leaves and greenery are good but not necessary.

```html
<!DOCTYPE html>
<html lang="en">
<head>
<meta charset="utf-8">
<title>The Hidden Weather Within – Cover Wrap</title>
<link rel="stylesheet" href="https://fonts.googleapis.com/css2?family=Cinzel+Decorative:wght@700&family=Cinzel:wght@400;700&family=Tinos&display=swap">
<style>
  :root {
    --stage: #2b2630;
    --ink: #3a2520;
    --cream: #fbfcf2;
    --leaf-pale: #e6f5b8;
    --leaf: #9ed43a;
    --leaf-deep: #4f9a17;
    --grass-dark: #2f5a12;
    --spine-top: #8a7c72;
    --spine-mid: #4a3d36;
    --spine-bottom: #2f2622;
    --spine-text: #f2eee8;
    --ornament: rgba(90, 70, 60, 0.18);
  }
  * { margin: 0; padding: 0; box-sizing: border-box; }
  html, body { width: 1200px; height: 900px; overflow: hidden; background: var(--stage); }
  .canvas { position: relative; width: 1200px; height: 900px; }
  .wrap {
    position: absolute; left: 51px; top: 74px;
    width: 1098px; height: 752px; display: flex;
  }
  .back-cover, .front-cover { position: relative; width: 517px; height: 752px; overflow: hidden; }
  .back-cover {
    background:
      radial-gradient(circle at 75% 88%, rgba(255,255,230,0.55) 0 60px, transparent 62px),
      radial-gradient(circle at 20% 80%, rgba(255,255,200,0.35) 0 90px, transparent 92px),
      linear-gradient(180deg, var(--cream) 0%, var(--cream) 30%, var(--leaf-pale) 50%, var(--leaf) 72%, var(--leaf-deep) 100%);
  }
  .front-cover {
    background: linear-gradient(180deg, var(--cream) 0%, var(--cream) 22%, var(--leaf-pale) 38%, var(--leaf) 50%);
  }
  .spine {
    width: 64px; height: 752px;
    background: linear-gradient(180deg, var(--spine-top) 0%, var(--spine-mid) 35%, var(--spine-bottom) 100%);
    display: flex; flex-direction: column; align-items: center; justify-content: space-between;
    padding: 24px 0 22px;
  }
  .spine-title, .spine-author {
    writing-mode: vertical-rl; color: var(--spine-text); white-space: nowrap;
  }
  .spine-title { font-family: "Cinzel", serif; font-weight: 700; font-size: 25px; letter-spacing: 0.5px; }
  .spine-author { font-family: "Cinzel", serif; font-weight: 400; font-size: 24px; }

  .title-block { position: absolute; left: 0; width: 100%; text-align: center; color: var(--ink); }
  .title-big { font-family: "Cinzel Decorative", serif; font-weight: 700; line-height: 1; display: block; }
  .title-small { font-family: "Cinzel", serif; font-weight: 700; line-height: 1; display: block; }

  .back-cover .title-block { top: 46px; }
  .back-cover .title-big { font-size: 50px; }
  .back-cover .title-small { font-size: 28px; margin: 18px 0 16px; }

  .synopsis {
    position: absolute; left: 30px; right: 30px; top: 278px;
    font-family: "Tinos", serif; font-size: 15.6px; line-height: 21px;
    color: var(--ink); text-align: center;
  }

  .ornament { position: absolute; left: 20px; width: 477px; height: 50px; }
  .ornament-top { top: 12px; }
  .ornament-bottom { top: 246px; }
  .author-name {
    position: absolute; top: 58px; left: 0; width: 100%; text-align: center;
    font-family: "Cinzel", serif; font-size: 29px; color: var(--ink); letter-spacing: 0.5px;
  }
  .front-cover .title-block { top: 100px; }
  .front-cover .title-big { font-size: 56px; }
  .front-cover .title-small { font-size: 30px; margin: 10px 0 8px; }

  .cover-photo { position: absolute; left: 0; top: 270px; width: 517px; height: 482px; }
</style>
</head>
<body>
<main class="canvas">
  <section class="wrap">
    <article class="back-cover">
      <h2 class="title-block">
        <span class="title-big">THE HIDDEN</span>
        <span class="title-small">WEATHER</span>
        <span class="title-big">WITHIN</span>
      </h2>
      <p class="synopsis">The Hidden Weather Within is an acutely honest and often highly entertaining memoir by Dorothea Quill about life with Asperger's Syndrome. The book follows Dorothea in exploring her past and takes the reader with her on her journey to receiving and accepting her diagnosis. Instead of rehashing widely available Asperger's information, Dorothea focuses on discussing the thoughts, feelings and ideas that go along with being an Aspie, giving us a rare peek into what it really feels like to be a person on the spectrum. A must read for all those who enjoy deep personal stories or have a loved one on the spectrum that they wish to understand better.</p>
    </article>

    <aside class="spine">
      <span class="spine-title">THE HIDDEN WEATHER WITHIN</span>
      <span class="spine-author">DOROTHEA QUILL</span>
    </aside>

    <article class="front-cover">
      <svg class="cover-photo" viewBox="0 0 517 482" role="img" aria-label="Photo of the author lying in tall green grass, writing in a notebook">
        <defs>
          <linearGradient id="grass" x1="0" y1="0" x2="0" y2="1">
            <stop offset="0" stop-color="#9ed43a" stop-opacity="0"/>
            <stop offset="0.15" stop-color="#7fbf2c"/>
            <stop offset="0.6" stop-color="#4f9a17"/>
            <stop offset="1" stop-color="#2f5a12"/>
          </linearGradient>
          <radialGradient id="figure" cx="0.55" cy="0.55" r="0.45">
            <stop offset="0" stop-color="#b99a70" stop-opacity="0.55"/>
            <stop offset="1" stop-color="#b99a70" stop-opacity="0"/>
          </radialGradient>
        </defs>
        <rect width="517" height="482" fill="url(#grass)"/>
        <rect width="517" height="482" fill="url(#figure)"/>
      </svg>
      <svg class="ornament ornament-top" viewBox="0 0 477 50" role="img" aria-label="Scrollwork ornament">
        <rect x="0" y="10" width="477" height="30" rx="15" fill="var(--ornament)"/>
      </svg>
      <p class="author-name">DOROTHEA QUILL</p>
      <h1 class="title-block">
        <span class="title-big">THE HIDDEN</span>
        <span class="title-small">WEATHER</span>
        <span class="title-big">WITHIN</span>
      </h1>
      <svg class="ornament ornament-bottom" viewBox="0 0 477 50" role="img" aria-label="Scrollwork ornament">
        <rect x="0" y="10" width="477" height="30" rx="15" fill="var(--ornament)"/>
      </svg>
    </article>
  </section>
</main>
</body>
</html>
```